Ferncrest Dental, LLC business card project

Business card to be designed with current logo.
Dental office- please keep design of card that looks clean and professional.
Please include the following info:
Ferncrest Dental, LLC
Dr. Lorna Pettigrew
2871 Marlowe Street
Ridgemoor, OR 97381
503-555-0193
ferncrestdental.office@examplemail.test
Hello everyone-
Reason: Just got back from overseas- will look at all designs and provide feedback. Thank you!
Reason: Polling my friends for the final selection-
thank you to all those that participated- so many talented designers!

```html
<!DOCTYPE html>
<html lang="en">
<head>
<meta charset="utf-8">
<title>Ferncrest Dental, LLC – Business Card</title>
<link rel="stylesheet" href="https://fonts.googleapis.com/css2?family=Ubuntu:wght@400;700&display=swap">
<style>
  :root {
    --bg-top: #8f8f8f;
    --bg-bottom: #f4f4f4;
    --green-dark: #5b9a3a;
    --green-mid: #76ae52;
    --green-light: #a3cc84;
    --lime: #a9cf3c;
    --lime-edge: #5e9a2c;
    --white: #ffffff;
    --ink-green: #7cb342;
    --paper-shade: #eeeeee;
  }
  * { box-sizing: border-box; margin: 0; padding: 0; }
  html, body { width: 1200px; height: 861px; overflow: hidden; }
  body {
    background: linear-gradient(180deg, var(--bg-top) 0%, #c9c9c9 45%, var(--bg-bottom) 100%);
    font-family: "Ubuntu", sans-serif;
    position: relative;
  }
  .card {
    position: absolute;
    top: 290px;
    width: 500px;
    height: 286px;
    border-radius: 16px;
    overflow: hidden;
    box-shadow: 0 10px 24px rgba(0,0,0,0.25);
  }
  .card--front {
    left: 60px;
    background: linear-gradient(200deg, var(--green-light) 0%, var(--green-mid) 40%, var(--green-dark) 100%);
  }
  .card--back {
    left: 640px;
    background: linear-gradient(160deg, var(--white) 55%, var(--paper-shade) 100%);
  }
  .brand {
    display: flex;
    align-items: center;
    gap: 10px;
    color: var(--ink-green);
    font-weight: 400;
    white-space: nowrap;
  }
  .brand__dot {
    width: 14px; height: 14px;
    border-radius: 50%;
    background: var(--ink-green);
    flex: none;
  }
  .front-band {
    position: absolute;
    left: 0; right: 0;
    top: 92px;
    height: 80px;
    background: var(--white);
    display: flex;
    align-items: center;
    padding-left: 30px;
  }
  .front-band .brand { font-size: 34px; }
  .back-brand {
    position: absolute;
    top: 38px;
    right: 26px;
  }
  .back-brand .brand { font-size: 24px; }
  .name-band {
    position: absolute;
    left: 0; right: 0;
    top: 90px;
    height: 80px;
    background: linear-gradient(90deg, var(--green-dark), var(--green-mid) 60%, var(--green-light));
  }
  .name-box {
    position: absolute;
    left: 0;
    top: 10px;
    height: 52px;
    padding: 0 22px 0 28px;
    background: var(--lime);
    color: var(--white);
    font-weight: 700;
    font-size: 24px;
    display: flex;
    align-items: center;
  }
  .contacts {
    position: absolute;
    left: 0;
    top: 190px;
    list-style: none;
  }
  .contact {
    display: flex;
    align-items: center;
    gap: 8px;
    height: 20px;
    margin-bottom: 10px;
    padding: 0 12px 0 28px;
    background: var(--lime);
    border-right: 5px solid var(--lime-edge);
    color: var(--white);
    font-size: 12px;
    font-weight: 700;
    width: max-content;
    white-space: nowrap;
  }
  .contact svg { width: 12px; height: 12px; fill: var(--white); flex: none; }
</style>
</head>
<body>
  <section class="card card--front" aria-label="Card front">
    <div class="front-band">
      <div class="brand"><span class="brand__dot"></span>Ferncrest Dental, LLC</div>
    </div>
  </section>

  <section class="card card--back" aria-label="Card back">
    <div class="back-brand">
      <div class="brand"><span class="brand__dot"></span>Ferncrest Dental, LLC</div>
    </div>
    <div class="name-band">
      <div class="name-box">Dr. Lorna Pettigrew</div>
    </div>
    <ul class="contacts">
      <li class="contact">
        <svg viewBox="0 0 12 12" aria-hidden="true"><path d="M6 1 0.5 6H2v5h3V8h2v3h3V6h1.5z"/></svg>
        2871 Marlowe Street Ridgemoor, OR 97381
      </li>
      <li class="contact">
        <svg viewBox="0 0 12 12" aria-hidden="true"><path d="M2.5 1 4.5 3.2 3.5 4.6C4.2 6 6 7.8 7.4 8.5L8.8 7.5 11 9.5 9.6 11C5 10.5 1.5 7 1 2.4z"/></svg>
        503-555-0193
      </li>
      <li class="contact">
        <svg viewBox="0 0 12 12" aria-hidden="true"><path d="M1 2.5h10v7H1z M1 2.5 6 6.5 11 2.5" stroke="#5e9a2c" stroke-width="0.8"/></svg>
        ferncrestdental.office@examplemail.test
      </li>
    </ul>
  </section>
</body>
</html>
```